Magnetic car sign for Pillarwise Structural Advisors

I already have a logo, however I now need a design for a magnetic car sign. My company is Pillarwise Structural Advisors, and I am located in Perth, Western Australia. I operate in the building and construction industry. I work largely with architects, building designers, builders, and engineers.

Target Market(s)

Everyone

Industry/Entity Type

It Company

Requirements
Nice to have
• My car is gun metal grey (dark grey). I want to sign to be based on a dark background so that it blends in with the car.

```html
<!DOCTYPE html>
<html lang="en">
<head>
<meta charset="utf-8">
<title>Pillarwise Structural Advisors – Car Sign</title>
<link rel="stylesheet" href="https://fonts.googleapis.com/css2?family=Open+Sans:wght@400&display=swap">
<style>
  :root {
    --bg: #4a4a4a;
    --ink: #ffffff;
    --ink-soft: #eeeeee;
  }
  * { margin: 0; padding: 0; box-sizing: border-box; }
  html, body {
    width: 1200px;
    height: 787px;
    overflow: hidden;
    background: var(--bg);
  }
  .sign {
    position: relative;
    width: 1200px;
    height: 787px;
    background: var(--bg);
    font-family: "Open Sans", Arial, sans-serif;
    color: var(--ink);
  }
  .brand {
    position: absolute;
    left: 160px;
    top: 205px;
    display: flex;
    align-items: center;
    gap: 44px;
  }
  .brand-mark {
    width: 170px;
    height: 170px;
    border: 6px solid var(--ink);
    border-radius: 50%;
    flex: none;
  }
  .brand-name {
    font-weight: 400;
    font-size: 52px;
    line-height: 1.22;
    letter-spacing: 3px;
    text-transform: uppercase;
    color: var(--ink);
  }
  .contact {
    position: absolute;
    display: flex;
    align-items: center;
    gap: 30px;
    font-size: 50px;
    font-weight: 400;
    letter-spacing: 1px;
    color: var(--ink-soft);
  }
  .contact-web { left: 187px; top: 446px; }
  .contact-phone { left: 343px; top: 547px; letter-spacing: 3px; }
  .contact-icon { width: 72px; height: 72px; flex: none; }
</style>
</head>
<body>
  <main class="sign">
    <div class="brand">
      <span class="brand-mark"></span>
      <h1 class="brand-name">Pillarwise<br>Structural Advisors</h1>
    </div>

    <p class="contact contact-web">
      <svg class="contact-icon" viewBox="0 0 72 72" aria-hidden="true">
        <circle cx="36" cy="36" r="33" fill="none" stroke="#fff" stroke-width="3"/>
        <rect x="27" y="17" width="18" height="38" rx="3" fill="none" stroke="#fff" stroke-width="3"/>
        <rect x="31" y="22" width="10" height="11" fill="#fff"/>
        <circle cx="32" cy="39" r="1.8" fill="#fff"/><circle cx="36" cy="39" r="1.8" fill="#fff"/><circle cx="40" cy="39" r="1.8" fill="#fff"/>
        <circle cx="32" cy="44" r="1.8" fill="#fff"/><circle cx="36" cy="44" r="1.8" fill="#fff"/><circle cx="40" cy="44" r="1.8" fill="#fff"/>
        <circle cx="32" cy="49" r="1.8" fill="#fff"/><circle cx="36" cy="49" r="1.8" fill="#fff"/><circle cx="40" cy="49" r="1.8" fill="#fff"/>
      </svg>
      <span>www.pillarwisesa.com</span>
    </p>

    <p class="contact contact-phone">
      <svg class="contact-icon" viewBox="0 0 72 72" aria-hidden="true">
        <circle cx="36" cy="36" r="33" fill="none" stroke="#fff" stroke-width="3"/>
        <rect x="22" y="24" width="28" height="19" rx="2" fill="none" stroke="#fff" stroke-width="3"/>
        <path d="M16 47 H56 L53 51 H19 Z" fill="none" stroke="#fff" stroke-width="3" stroke-linejoin="round"/>
      </svg>
      <span>0400 555 187</span>
    </p>
  </main>
</body>
</html>
```